Morning Harbor Bible Fellowship needs a new Business Card/Letterhead Suite

***** IT DOES NOT HAVE TO FEATURE GREEN AND BROWN in order to be a successful design*****

****FONTS: SF New Republic, 'Morning Harbor'; Nexa Light, 'Bible Fellowship'****

***We have two locations, with two addresses. So the business card AND letterhead need to include two sets of address information***

We are a growing church in New York in need of a new stationary suite. We have recently adopted a new logo (via a successful ArtHivePro project) and need new business cards, letterhead, envelopes, and folders.

We would like to see creative, original designs that are modern and clean/elegant (NOT dated "churchy" graphics that are cheesy).

We need this project worked on immediately, as we need to print new business cards for upcoming programs we have on our schedule. So, the designs need to be solid so that we can move quickly throughout the revision process toward print.

We'd also need editables files, so that we can drop in other staff members names/phone numbers, to be able to print cards for those staff needing them.

Requirements
Must have
• Our logo
• Must be given to us in an editable format (to change names)
Nice to have
• Some examples on grey, or recycled, card stock
• card stock (background) does not have to be white
Should not have
• Any extraneous logo's or symbols

```html
<!DOCTYPE html>
<html lang="en">
<head>
<meta charset="utf-8">
<title>Morning Harbor Bible Fellowship – Business Card</title>
<link rel="stylesheet" href="https://fonts.googleapis.com/css2?family=Montserrat:wght@300;400;500&display=swap">
<style>
  :root {
    --page-bg: #e4e2dd;
    --panel-dark: #34332a;
    --panel-mid: #4d4c3e;
    --panel-light: #6a6953;
    --frost-a: #d3d0c8;
    --frost-b: #e3e1db;
    --ink-light: #f2f1ec;
    --ink-soft: #dddcd3;
    --brand-green: #2f4a23;
    --stalk-a: #5d7a43;
    --stalk-b: #3e5a2c;
  }
  * { margin: 0; padding: 0; box-sizing: border-box; }
  html, body { width: 1200px; height: 969px; overflow: hidden; }
  body {
    background: var(--page-bg);
    font-family: "Montserrat", sans-serif;
    position: relative;
  }
  .business-card {
    position: absolute;
    left: 100px;
    top: 200px;
    width: 1000px;
    height: 570px;
    background: linear-gradient(120deg, var(--frost-a), var(--frost-b));
    box-shadow: 0 18px 40px rgba(0,0,0,0.18);
    overflow: hidden;
  }
  .contact-panel {
    position: absolute;
    left: 0; top: 0;
    width: 455px;
    height: 100%;
    background: linear-gradient(90deg, var(--panel-dark) 0%, var(--panel-mid) 60%, var(--panel-light) 100%);
    color: var(--ink-light);
    padding: 84px 0 0 64px;
  }
  .staff-name {
    font-size: 31px;
    font-weight: 500;
    letter-spacing: 1px;
    line-height: 1;
  }
  .staff-title {
    font-size: 20px;
    font-weight: 400;
    color: var(--ink-soft);
    margin-top: 10px;
    letter-spacing: 0.5px;
  }
  .address {
    font-size: 20px;
    line-height: 27px;
    margin-top: 18px;
    color: var(--ink-soft);
  }
  .address + .address { margin-top: 10px; }
  .contact-list {
    list-style: none;
    margin-top: 16px;
    font-size: 20px;
    line-height: 29px;
    color: var(--ink-soft);
  }
  .contact-list li { display: flex; align-items: center; }
  .contact-list svg {
    width: 17px; height: 17px;
    margin-right: 16px;
    fill: var(--ink-soft);
    flex: none;
  }
  .stalk-art {
    position: absolute;
    left: 424px;
    top: 0;
    width: 84px;
    height: 570px;
    background: linear-gradient(180deg, var(--stalk-a) 0%, var(--stalk-b) 45%, rgba(62,90,44,0.25) 100%);
    opacity: 0.5;
  }
  .brand-block {
    position: absolute;
    left: 520px;
    top: 232px;
    width: 440px;
    text-align: center;
    color: var(--brand-green);
  }
  .brand-name {
    font-size: 50px;
    font-weight: 400;
    letter-spacing: 0.5px;
    line-height: 1.1;
  }
  .brand-tagline {
    font-size: 22px;
    font-weight: 300;
    letter-spacing: 4px;
    text-transform: uppercase;
    margin-top: 8px;
  }
</style>
</head>
<body>
  <div class="business-card">
    <section class="contact-panel">
      <h1 class="staff-name">DANIEL REYES</h1>
      <p class="staff-title">CEO/FOUNDER</p>
      <p class="address">4120 Harbor View Road<br>Riverton, New York 12895</p>
      <p class="address">88 Lakeside Avenue<br>Port Ellis, New York 12902</p>
      <ul class="contact-list">
        <li>
          <svg viewBox="0 0 24 24" aria-hidden="true"><path d="M6.6 10.8a15.1 15.1 0 0 0 6.6 6.6l2.2-2.2a1 1 0 0 1 1-.25 11.4 11.4 0 0 0 3.6.57 1 1 0 0 1 1 1V20a1 1 0 0 1-1 1A17 17 0 0 1 3 4a1 1 0 0 1 1-1h3.5a1 1 0 0 1 1 1c0 1.25.2 2.45.57 3.57a1 1 0 0 1-.25 1z"/></svg>
          555 210 4837
        </li>
        <li>
          <svg viewBox="0 0 24 24" aria-hidden="true"><path d="M7 1h10a2 2 0 0 1 2 2v18a2 2 0 0 1-2 2H7a2 2 0 0 1-2-2V3a2 2 0 0 1 2-2zm0 3v14h10V4zm5 15.5a1.2 1.2 0 1 0 0 2.4 1.2 1.2 0 0 0 0-2.4z"/></svg>
          555 382 6190
        </li>
        <li>
          <svg viewBox="0 0 24 24" aria-hidden="true"><path d="M6 2h10l2 2v5H6zM3 10h18a2 2 0 0 1 2 2v8H1v-8a2 2 0 0 1 2-2zm3 4v2h4v-2zm8 0v2h2v-2zm3 0v2h2v-2z"/></svg>
          555 746 2051
        </li>
        <li>
          <svg viewBox="0 0 24 24" aria-hidden="true"><path d="M2 5h20v14H2zm2 2v.5l8 5.5 8-5.5V7zm0 3v7h16v-7l-8 5.5z"/></svg>
          name@morningharbor.org
        </li>
        <li>
          <svg viewBox="0 0 24 24" aria-hidden="true"><path d="M12 2a10 10 0 1 0 0 20 10 10 0 0 0 0-20zm6.9 6h-3a15 15 0 0 0-1.3-3.9A8 8 0 0 1 18.9 8zM12 4c.8 1.1 1.5 2.5 1.9 4h-3.8c.4-1.5 1.1-2.9 1.9-4zM4.3 14a8 8 0 0 1 0-4h3.4a16 16 0 0 0 0 4zm.8 2h3a15 15 0 0 0 1.3 3.9A8 8 0 0 1 5.1 16zm3-8h-3a8 8 0 0 1 4.3-3.9A15 15 0 0 0 8.1 8zM12 20c-.8-1.1-1.5-2.5-1.9-4h3.8c-.4 1.5-1.1 2.9-1.9 4zm2.3-6H9.7a14 14 0 0 1 0-4h4.6a14 14 0 0 1 0 4zm.3 5.9a15 15 0 0 0 1.3-3.9h3a8 8 0 0 1-4.3 3.9zm1.7-5.9a16 16 0 0 0 0-4h3.4a8 8 0 0 1 0 4z"/></svg>
          www.morningharbor.org
        </li>
      </ul>
    </section>
    <div class="stalk-art" role="img" aria-label="Decorative illustration of slender green wheat stalks rising along the panel edge"></div>
    <div class="brand-block">
      <p class="brand-name">Morning Harbor</p>
      <p class="brand-tagline">Bible Fellowship</p>
    </div>
  </div>
</body>
</html>
```